Presentation Folder

We want to create a clean, modern folder for our three companies- A single folder. Feel free to be as creative as possible. We are good with some color, but want it to stay clean and modern. See our website veltrimhire.net for more idea of the vibe. I've attached all 3 logos to be used as well as our new business cards

Target Market(s)

Senior executives

Industry/Entity Type

Business

Font styles to use
Serif
Sans Serif

Colors
85acd3
3176b5
0455a3
0792cd
34a6d7
85cae6

Requirements
Must have
• All 3 logos websites and phone numbers (see business card).

```html
<!DOCTYPE html>
<html lang="en">
<head>
<meta charset="utf-8">
<title>Presentation Folder and Brochure</title>
<link rel="stylesheet" href="https://fonts.googleapis.com/css2?family=Open+Sans:wght@400;600;700&display=swap">
<style>
  :root {
    --bg: #e4e5e7;
    --paper: #ffffff;
    --navy: #0455a3;
    --blue: #3176b5;
    --sky: #85acd3;
    --cyan: #0792cd;
    --aqua: #85cae6;
    --tan: #9a7a5c;
    --ink: #222;
    --mist: #e9edf5;
  }
  * { box-sizing: border-box; margin: 0; padding: 0; }
  html, body { width: 1200px; height: 726px; overflow: hidden; }
  body {
    background: var(--bg);
    font-family: "Open Sans", Arial, sans-serif;
    position: relative;
  }
  .piece-label {
    position: absolute;
    font-size: 15px;
    color: var(--ink);
    letter-spacing: .5px;
  }
  .piece-label--folder { left: 64px; top: 140px; }
  .piece-label--brochure { left: 1010px; top: 548px; }

  /* Folder */
  .folder {
    position: absolute;
    left: 60px; top: 170px;
    width: 720px; height: 500px;
    display: flex;
    box-shadow: 0 6px 18px rgba(0,0,0,.18);
  }
  .folder-panel {
    position: relative;
    width: 360px; height: 500px;
    background: var(--paper);
    overflow: hidden;
    border-bottom: 12px solid var(--navy);
  }
  .folder-panel--back { border-right: 1px solid #dcdde0; }

  .tagline-band {
    position: absolute;
    left: -20px; top: 52px;
    width: 400px; height: 54px;
    background: var(--navy);
    transform: rotate(-8deg);
    display: flex; align-items: center; justify-content: center;
  }
  .tagline {
    color: #fff;
    font-weight: 600;
    font-size: 13px;
    letter-spacing: 1.5px;
  }
  .contact-list {
    position: absolute;
    top: 170px; left: 0; width: 100%;
    display: flex; flex-direction: column; align-items: center;
    gap: 46px;
  }
  .contact {
    text-align: center;
    display: flex; flex-direction: column; align-items: center; gap: 4px;
  }
  .brand-name {
    display: flex; align-items: center; gap: 6px;
    font-weight: 700;
    font-size: 18px;
    color: var(--navy);
    letter-spacing: .5px;
  }
  .brand-name .mark {
    width: 10px; height: 10px;
    background: var(--blue);
  }
  .contact-line {
    font-size: 10px;
    font-weight: 600;
    color: var(--blue);
    line-height: 1.3;
  }

  .map-field {
    position: absolute;
    left: 0; top: 0;
    width: 100%; height: 210px;
    background: radial-gradient(ellipse at 50% 40%, #e3e7ef 0%, #f3f5f9 55%, #ffffff 100%);
  }
  .brand-strip {
    position: absolute;
    left: 0; top: 38px;
    width: 100%; height: 54px;
    background: rgba(220,224,238,.75);
    display: flex; align-items: center; justify-content: space-around;
    padding: 0 10px;
  }
  .brand-strip .brand-name { font-size: 12px; gap: 4px; }
  .brand-strip .brand-name .mark { width: 7px; height: 7px; }

  /* Brochure */
  .brochure {
    position: absolute;
    left: 810px; top: 110px;
    width: 330px; height: 420px;
    background: var(--paper);
    box-shadow: 0 6px 18px rgba(0,0,0,.18);
    overflow: hidden;
  }
  .brochure-photo {
    position: absolute; inset: 0;
    background: linear-gradient(170deg, #f4f6f3 0%, #dfe3e0 35%, #9fb5a8 60%, #7d8a8e 80%, #c9ccc8 100%);
  }
  .brochure-tagline {
    position: absolute;
    right: 14px; top: 34px;
    font-size: 11px; font-weight: 700;
    color: var(--navy);
    letter-spacing: 1px;
  }
  .brochure .brand-strip { top: 56px; height: 46px; background: rgba(255,255,255,.72); }
  .brochure .brand-strip .brand-name { font-size: 10.5px; }
</style>
</head>
<body>
  <div class="piece-label piece-label--folder">FOLDER</div>
  <div class="piece-label piece-label--brochure">BROCHURE</div>

  <section class="folder">
    <div class="folder-panel folder-panel--back">
      <div class="tagline-band"><span class="tagline">PREPARE | PLAN | SUPPORT</span></div>
      <div class="contact-list">
        <div class="contact">
          <div class="brand-name"><span class="mark"></span>HALVERN ACADEMY</div>
          <div class="contact-line">www.halvernacademy.org<br>877.555.0142</div>
        </div>
        <div class="contact">
          <div class="brand-name"><span class="mark"></span>VELTRIM HIRE</div>
          <div class="contact-line">www.veltrimhire.net<br>800.555.0173</div>
        </div>
        <div class="contact">
          <div class="brand-name"><span class="mark"></span>CORVANE ASSOCIATES</div>
          <div class="contact-line">www.corvaneassociates.com<br>800.555.0196</div>
        </div>
      </div>
    </div>

    <div class="folder-panel folder-panel--front">
      <div class="map-field" role="img" aria-label="Faint grey world map across the top of the cover"></div>
      <div class="brand-strip">
        <div class="brand-name"><span class="mark"></span>HALVERN</div>
        <div class="brand-name"><span class="mark"></span>VELTRIM HIRE</div>
        <div class="brand-name"><span class="mark"></span>CORVANE</div>
      </div>
    </div>
  </section>

  <section class="brochure">
    <div class="brochure-photo" role="img" aria-label="Photo of four students walking together along a bright campus walkway carrying books and bags"></div>
    <div class="brochure-tagline">PREPARE | PLAN | SUPPORT</div>
    <div class="brand-strip">
      <div class="brand-name"><span class="mark"></span>HALVERN</div>
      <div class="brand-name"><span class="mark"></span>VELTRIM HIRE</div>
      <div class="brand-name"><span class="mark"></span>CORVANE</div>
    </div>
  </section>
</body>
</html>
```